Skatepark, and Teenage Music/Recreation Venue needs logo, business card and letterhead. Website desi

- Logo, Letterhead & Business Card design for a new start Skatepark and Youth Venue called "The Orbit" (Pty.Ltd company) in Australia.

- Website and App design will follow within 6-months.

- Facility centered around world class skatepark which incorporates the use of innovative technology applications to enhance consumer experience, it will also provide a live entertainment & music venue for teenagers.

- Appearance should appeal to the 'mature' teenage population, the aim is provide an excellent membership experience which can be associated with the club brand.

Overall the design should communicate:
Excitement, energy, exclusivity and style

- Clean and modern fonts and styling preferred.
- Logos the I personally like: Brinmore, Quellstone, (but they don't have to be round!)
- Generally I prefer understated business cards that are subtlety/elegently distinct
- ideally the logo would be expected to standalone if no text were available. (if that makes sense?)

Business

The Orbit

```html
<!DOCTYPE html>
<html lang="en">
<head>
<meta charset="utf-8">
<title>The Orbit — Stationery Set</title>
<link rel="stylesheet" href="https://fonts.googleapis.com/css2?family=Questrial&display=swap">
<style>
  :root {
    --sky: #29a9e1;
    --violet: #682f8f;
    --slate: #818284;
    --paper: #ffffff;
    --stage-top: #ffffff;
    --stage-bottom: #d9d9d9;
    --shadow: rgba(0, 0, 0, 0.55);
  }
  * { margin: 0; padding: 0; box-sizing: border-box; }
  html, body { width: 1200px; height: 900px; overflow: hidden; }
  body {
    position: relative;
    background: linear-gradient(to bottom, var(--stage-top), var(--stage-bottom));
    font-family: "Questrial", "Century Gothic", sans-serif;
  }
  .brand-band {
    background: linear-gradient(to bottom, var(--sky) 20%, var(--violet));
  }
  .wordmark {
    position: absolute;
    display: flex;
    align-items: center;
    white-space: nowrap;
  }
  .wordmark__square { background: var(--slate); flex: none; }
  .wordmark__name { color: var(--sky); line-height: 1; }

  /* Letterhead */
  .letterhead {
    position: absolute;
    left: 43px; top: 187px;
    width: 525px; height: 678px;
    background: var(--paper);
    box-shadow: 4px 4px 6px var(--shadow);
  }
  .letterhead__top-band {
    position: absolute;
    left: 112px; top: 0;
    width: 413px; height: 63px;
    clip-path: polygon(0 0, 100% 0, 100% 100%, 48px 100%);
  }
  .letterhead__bottom-band {
    position: absolute;
    left: 0; bottom: 0;
    width: 100%; height: 37px;
  }
  .letterhead .wordmark { left: 20px; top: 22px; gap: 5px; }
  .letterhead .wordmark__square { width: 18px; height: 18px; }
  .letterhead .wordmark__name { font-size: 22px; }

  /* Primary logo */
  .logo-primary { left: 630px; top: 120px; gap: 14px; }
  .logo-primary .wordmark__square { width: 80px; height: 80px; }
  .logo-primary .wordmark__name { font-size: 96px; letter-spacing: -1px; }

  .logo-small { left: 636px; top: 333px; gap: 6px; }
  .logo-small .wordmark__square { width: 22px; height: 22px; }
  .logo-small .wordmark__name { font-size: 28px; }

  /* Business card */
  .business-card {
    position: absolute;
    left: 686px; top: 480px;
    width: 418px; height: 238px;
    background: var(--paper);
    box-shadow: 4px 4px 6px var(--shadow);
  }
  .business-card .wordmark { left: 12px; top: 34px; gap: 7px; }
  .business-card .wordmark__square { width: 28px; height: 28px; }
  .business-card .wordmark__name { font-size: 38px; }
  .business-card__details {
    position: absolute;
    left: 223px; top: 0;
    width: 195px; height: 100%;
    background: var(--slate);
    color: var(--paper);
    text-align: right;
    padding: 24px 17px 0 0;
  }
  .contact-group { margin-bottom: 14px; line-height: 0.95; }
  .contact-name { font-size: 34px; }
  .contact-line { font-size: 26px; }
</style>
</head>
<body>

  <section class="letterhead" aria-label="Letterhead">
    <div class="letterhead__top-band brand-band"></div>
    <div class="wordmark">
      <span class="wordmark__square"></span>
      <span class="wordmark__name">The Orbit</span>
    </div>
    <div class="letterhead__bottom-band brand-band"></div>
  </section>

  <div class="wordmark logo-primary" aria-label="The Orbit logo">
    <span class="wordmark__square"></span>
    <span class="wordmark__name">The Orbit</span>
  </div>

  <div class="wordmark logo-small" aria-label="The Orbit logo, small">
    <span class="wordmark__square"></span>
    <span class="wordmark__name">The Orbit</span>
  </div>

  <section class="business-card" aria-label="Business card">
    <div class="wordmark">
      <span class="wordmark__square"></span>
      <span class="wordmark__name">The Orbit</span>
    </div>
    <div class="business-card__details">
      <div class="contact-group">
        <div class="contact-name">Name</div>
        <div class="contact-line">Position</div>
      </div>
      <div class="contact-group">
        <div class="contact-line">Telephone</div>
        <div class="contact-line">Mobile</div>
      </div>
      <div class="contact-group">
        <div class="contact-line">Email</div>
        <div class="contact-line">Website</div>
      </div>
    </div>
  </section>

</body>
</html>
```